Healthcare IT firm needs classy and unique business care design

We need a business card design that incorporates our new logo design (attached) Prefer a purple based designed. I would really love to see something utilizing the "3D" version of the logo (purple on the reflective wall). I want something a little more than my logo printed along with a person's detailed contact information.
Contact Information for Business Card
Want something polished, professional, and a little unique in the design.
Colors
6b449b
Requirements
Must have
- Please use similar font as the logo design
Nice to have
- Would like to see the 3d version of my logo incorporated into the design.

```html
<!DOCTYPE html>
<html lang="en">
<head>
<meta charset="utf-8">
<title>Veluma Health Systems – Business Card</title>
<link rel="stylesheet" href="https://fonts.googleapis.com/css2?family=Lato:wght@400;700&family=Open+Sans:wght@400;600&display=swap">
<style>
  :root {
    --purple: #6b449b;
    --purple-light: #8a63bd;
    --ink: #1c1c1c;
    --muted: #444444;
    --card-white: #fbfbfb;
    --card-black: #151515;
    --silver: #d4d4d4;
    --page: #e9e6e1;
  }
  * { margin: 0; padding: 0; box-sizing: border-box; }
  html, body { width: 1200px; height: 942px; overflow: hidden; }
  body {
    background: var(--page);
    display: flex;
    align-items: center;
    justify-content: center;
    gap: 40px;
    font-family: "Open Sans", Arial, sans-serif;
  }
  .card {
    width: 560px;
    height: 320px;
    position: relative;
    box-shadow: 0 10px 28px rgba(0,0,0,0.22);
  }
  .card-front {
    background: linear-gradient(135deg, #ffffff 0%, var(--card-white) 55%, #eeeeee 100%);
    display: flex;
    align-items: center;
  }
  .front-brand {
    width: 270px;
    display: flex;
    align-items: center;
    justify-content: center;
    gap: 10px;
  }
  .brand-mark {
    width: 14px; height: 14px;
    background: var(--purple);
    flex: none;
  }
  .brand-name {
    font-family: "Lato", Arial, sans-serif;
    font-weight: 700;
    font-size: 24px;
    line-height: 1.15;
    color: var(--purple);
  }
  .divider {
    width: 2px;
    height: 190px;
    background: var(--purple);
  }
  .contact {
    padding-left: 32px;
  }
  .person-name {
    font-size: 30px;
    font-weight: 400;
    color: var(--ink);
    line-height: 1.1;
  }
  .job-title {
    margin-top: 6px;
    font-size: 14px;
    font-weight: 600;
    letter-spacing: 1.5px;
    color: var(--purple-light);
  }
  .contact-list {
    list-style: none;
    margin-top: 18px;
  }
  .contact-list li {
    display: flex;
    align-items: center;
    gap: 12px;
    font-size: 15px;
    color: var(--muted);
    margin-bottom: 8px;
  }
  .contact-list svg { width: 18px; height: 18px; fill: var(--purple-light); flex: none; }
  .card-back {
    background: radial-gradient(ellipse at 45% 30%, #3a3a3a 0%, #222 40%, var(--card-black) 80%);
    display: flex;
    align-items: center;
    justify-content: center;
    gap: 14px;
  }
  .card-back .brand-mark { background: var(--silver); width: 18px; height: 18px; }
  .card-back .brand-name { color: var(--silver); font-size: 32px; }
</style>
</head>
<body>
  <section class="card card-front">
    <div class="front-brand">
      <span class="brand-mark"></span>
      <span class="brand-name">Veluma Health<br>Systems</span>
    </div>
    <div class="divider"></div>
    <div class="contact">
      <p class="person-name">Your Name</p>
      <p class="job-title">JOB TITLE</p>
      <ul class="contact-list">
        <li>
          <svg viewBox="0 0 24 24" aria-hidden="true"><path d="M6.6 10.8a15.1 15.1 0 0 0 6.6 6.6l2.2-2.2a1 1 0 0 1 1-.25 11.4 11.4 0 0 0 3.6.57 1 1 0 0 1 1 1V20a1 1 0 0 1-1 1A17 17 0 0 1 3 4a1 1 0 0 1 1-1h3.5a1 1 0 0 1 1 1c0 1.25.2 2.45.57 3.57a1 1 0 0 1-.25 1z"/></svg>
          000 000 0000
        </li>
        <li>
          <svg viewBox="0 0 24 24" aria-hidden="true"><path d="M2 5h20v14H2z M2 5l10 8 10-8" stroke="#fbfbfb" stroke-width="1.5"/></svg>
          yourname@xyz.com
        </li>
        <li>
          <svg viewBox="0 0 24 24" aria-hidden="true"><path d="M12 2a7 7 0 0 0-7 7c0 5.2 7 13 7 13s7-7.8 7-13a7 7 0 0 0-7-7zm0 9.5A2.5 2.5 0 1 1 12 6.5a2.5 2.5 0 0 1 0 5z"/></svg>
          Your Address
        </li>
      </ul>
    </div>
  </section>

  <section class="card card-back">
    <span class="brand-mark"></span>
    <span class="brand-name">Veluma Health<br>Systems</span>
  </section>
</body>
</html>
```